Local business providing residential house cleaning services

We need a business card design that is "cute" or "cartoonish" while still maintaining a professional appeal. Tidy Lark Cleaners is the name. We would like to use a "pin up girl" or maid next to the name with a broom or vacuum cleaner. We want the look to have a 50's American look to it. We are not sure if we want the pin up girl in a maid outfit or with a broom or vacuum cleaner but we hope some of you will be able to take these ideas and be creative. If you have any questions at all please don't hesitate to message me so that we can get the best design possible. Thank you very much and I look forward to seeing some designs! Mona Pritchett

Target Market(s)

Upper class Americans that are busy and have money and want to come home to a clean house.

Industry/Entity Type

Cleaning Service

Contact Information for Business Card

Pin up girl incorporated into the card is a must.

Font styles to use
Decorative
Script

Requirements
Must have
• Pin up girl
Nice to have
• A crown used on the Q possibly.

```html
<!DOCTYPE html>
<html lang="en">
<head>
<meta charset="utf-8">
<title>Tidy Lark Cleaners – Business Card</title>
<link href="https://fonts.googleapis.com/css2?family=Source+Sans+3:wght@400;600&display=swap" rel="stylesheet">
<style>
  :root {
    --backdrop: #c6c6c6;
    --card: #ffffff;
    --ink: #333333;
    --accent: #4ab3cc;
    --bubble-light: #eaf5fb;
    --bubble-mid: #c4e3f2;
    --figure-top: #f1dcc8;
    --figure-mid: #d9d4cf;
    --figure-low: #a9a9a9;
  }
  html, body {
    margin: 0;
    padding: 0;
    width: 1200px;
    height: 1200px;
    overflow: hidden;
    background: var(--backdrop);
    font-family: "Source Sans 3", sans-serif;
  }
  .card {
    position: absolute;
    left: 191px;
    width: 818px;
    height: 478px;
    background: var(--card);
    box-shadow: 2px 3px 4px rgba(0,0,0,0.35);
    overflow: hidden;
  }
  .card--front { top: 74px; }
  .card--back { top: 633px; }

  .bubbles {
    position: absolute;
    inset: 0;
    background:
      radial-gradient(ellipse 45% 35% at 72% 92%, var(--bubble-mid) 0%, rgba(196,227,242,0) 70%),
      linear-gradient(to bottom, rgba(255,255,255,0) 45%, var(--bubble-light) 75%, var(--bubble-mid) 100%);
  }
  .card--back .bubbles {
    background:
      radial-gradient(ellipse 45% 35% at 72% 92%, var(--bubble-mid) 0%, rgba(196,227,242,0) 70%),
      linear-gradient(to bottom, #fbfdfe 0%, var(--bubble-light) 60%, var(--bubble-mid) 100%);
  }

  .wordmark {
    position: absolute;
    margin: 0;
    color: var(--ink);
    font-weight: 600;
    text-align: right;
  }
  .wordmark__main, .wordmark__sub {
    position: absolute;
    right: 0;
    line-height: 1;
    white-space: nowrap;
  }
  .wordmark__sub { letter-spacing: 0.28em; text-transform: uppercase; }

  .card--front .wordmark { left: 60px; width: 242px; top: 236px; }
  .card--front .wordmark__main { top: 0; font-size: 58px; }
  .card--front .wordmark__sub { top: 70px; font-size: 17px; right: -8px; }

  .card--back .wordmark { left: 100px; width: 398px; top: 238px; }
  .card--back .wordmark__main { top: 0; font-size: 94px; }
  .card--back .wordmark__sub { top: 104px; font-size: 26px; right: -14px; }

  .figure {
    position: absolute;
    border-radius: 44% 44% 10px 10px / 18% 18% 10px 10px;
    background: linear-gradient(to bottom, var(--figure-top) 0%, var(--figure-mid) 55%, var(--figure-low) 100%);
    opacity: 0.75;
  }
  .card--front .figure { left: 312px; top: 160px; width: 72px; height: 162px; }
  .card--back .figure { left: 512px; top: 104px; width: 112px; height: 252px; }

  .divider {
    position: absolute;
    left: 442px;
    top: 130px;
    width: 3px;
    height: 220px;
    background: var(--accent);
  }
  .contact {
    position: absolute;
    left: 488px;
    top: 174px;
    color: var(--ink);
  }
  .contact__name { margin: 0; font-size: 31px; font-weight: 400; line-height: 1; }
  .contact__title { margin: 6px 0 0; font-size: 18px; color: var(--accent); line-height: 1; }
  .contact__list { list-style: none; padding: 0; margin: 24px 0 0; }
  .contact__item { display: flex; align-items: center; gap: 12px; font-size: 19px; height: 35px; }
  .contact__icon { width: 22px; height: 16px; flex: none; }
</style>
</head>
<body>

<section class="card card--front">
  <div class="bubbles" role="img" aria-label="Soft background of light blue soap bubbles"></div>
  <h1 class="wordmark">
    <span class="wordmark__main">Tidy Lark</span>
    <span class="wordmark__sub">Cleaners</span>
  </h1>
  <div class="figure" role="img" aria-label="Cartoon pin-up maid with red hair, black dress, white apron and a broom"></div>
  <div class="divider"></div>
  <div class="contact">
    <h2 class="contact__name">Your Name</h2>
    <p class="contact__title">Job Title</p>
    <ul class="contact__list">
      <li class="contact__item">
        <svg class="contact__icon" viewBox="0 0 22 16" aria-hidden="true">
          <path d="M1 5 Q11 -1 21 5 L19 7 L15 6 L15 4 Q11 3 7 4 L7 6 L3 7 Z" fill="#4ab3cc"/>
          <rect x="4" y="8" width="14" height="8" rx="1" fill="#4ab3cc"/>
          <circle cx="11" cy="12" r="2.2" fill="#fff"/>
        </svg>
        000 000 0000
      </li>
      <li class="contact__item">
        <svg class="contact__icon" viewBox="0 0 22 16" aria-hidden="true">
          <rect x="0" y="2" width="22" height="13" fill="#4ab3cc"/>
          <path d="M0 2 L11 10 L22 2" fill="none" stroke="#fff" stroke-width="1.5"/>
        </svg>
        youremail@xyz.com
      </li>
    </ul>
  </div>
</section>

<section class="card card--back">
  <div class="bubbles" role="img" aria-label="Soft background of light blue soap bubbles"></div>
  <h1 class="wordmark">
    <span class="wordmark__main">Tidy Lark</span>
    <span class="wordmark__sub">Cleaners</span>
  </h1>
  <div class="figure" role="img" aria-label="Cartoon pin-up maid with red hair, black dress, white apron and a broom"></div>
</section>

</body>
</html>
```